Cedar Row Maintenance and Concierge Flyer

We need a flyer for cedar row maintenance and concierge service. We specialize in and provide residential maintenance and errand services to retired and semi retired persons living in the Lake Norman area. The services we include:
Lighting and plumbing repairs
Ceiling fan installation
Handicap accessories
Locks and security
Picture hanging
Hang blinds
Furniture arrangement / assembly
Pressure washing
Battery Jump start
and more...

Our Concierge services include:
Errand running
Grocery shopping
Wellness Checks
Dog Walk
Garbage Collection
and more...

We offer monthly service agreements and 24/7 access
Call text or e-mail for more information
704.555.0187
1cedarrowmaint@quillpostmail.com

The design should invoke a sense of trust and a customer service driven mission

Target Market(s)

Residential maintenance

Industry/Entity Type

Property Maintenance

Contact Information for Business Card

Derek Halvorsen
48176 Quimby Ferrel Rd.
Cornelius NC 28031
704.555.0187
with uploaded logo

Requirements
Nice to have
• Would like a postcard size flyer. Front and back
Should not have
• No pics of of people wearing hard hats or pics of blueprints. No pics of commercial or industrial maintenance.

```html
<!DOCTYPE html>
<html lang="en">
<head>
<meta charset="utf-8">
<title>Cedar Row Maintenance and Concierge – Postcard Flyer</title>
<link href="https://fonts.googleapis.com/css2?family=Fira+Sans+Condensed:wght@700;800&family=Montserrat:wght@700&family=Roboto+Condensed:wght@400;500;700&display=swap" rel="stylesheet">
<style>
  :root{
    --red:#d42027;
    --ink:#111111;
    --wood:#3d3d3d;
    --wood-dark:#262626;
    --stripe:#5a5a5a;
    --white:#ffffff;
    --page:#e6e6e6;
    --logo-grey:#6f6f6f;
    --leaf:#3f8f2c;
    --leaf-dark:#1f4d18;
    --grass:#5d9b34;
    --path:#b9bcc0;
  }
  *{box-sizing:border-box;margin:0;padding:0}
  html,body{width:1200px;height:1200px;overflow:hidden;background:var(--page)}
  body{position:relative;font-family:"Roboto Condensed",sans-serif}

  .card{position:absolute;left:174px;width:853px;height:568px;background:var(--white);overflow:hidden;box-shadow:0 2px 8px rgba(0,0,0,.25)}
  .card--front{top:24px}
  .card--back{top:608px}
  .shapes{position:absolute;inset:0;width:100%;height:100%}

  .photo{position:absolute}
  .photo--park{inset:0;
    background:linear-gradient(180deg,#2d6a1f 0%,var(--leaf) 35%,#6fae3a 62%,var(--leaf-dark) 80%,var(--path) 92%,#9ea3a6 100%);
    clip-path:polygon(506px 0,100% 0,100% 100%,556px 100%,470px 300px)}
  .photo--walk{left:0;top:238px;width:540px;height:242px;
    background:linear-gradient(170deg,var(--grass) 0%,#c7ccd0 25%,#aab0b6 40%,var(--grass) 55%,#4c8a28 100%);
    clip-path:polygon(0 0,468px 0,522px 100%,0 100%)}

  .logo{position:absolute;display:flex;align-items:center;gap:12px}
  .logo__dot{border-radius:50%;background:var(--red);flex:none}
  .logo__name{font-family:"Roboto Condensed",sans-serif;font-weight:400;color:var(--logo-grey);line-height:1}
  .logo__tag{font-family:"Roboto Condensed",sans-serif;font-weight:400;color:var(--logo-grey);letter-spacing:.3px}
  .logo--front{left:32px;top:22px}
  .logo--front .logo__dot{width:62px;height:62px}
  .logo--front .logo__name{font-size:46px}
  .logo--front .logo__tag{font-size:14.5px;margin-top:6px}
  .logo--back{left:656px;top:502px;gap:7px}
  .logo--back .logo__dot{width:34px;height:34px}
  .logo--back .logo__name{font-size:25px}
  .logo--back .logo__tag{font-size:8px;margin-top:3px}

  .intro{position:absolute;left:20px;top:137px;width:360px;font-size:13.5px;line-height:17px;color:var(--ink);font-weight:500}
  .headline{position:absolute;left:17px;top:220px;font-family:"Fira Sans Condensed",sans-serif;font-weight:800;font-size:34px;line-height:35px;color:var(--white);letter-spacing:.2px}

  .tab-title{position:absolute;font-family:"Montserrat",sans-serif;font-weight:700;color:var(--white);white-space:nowrap}
  .tab-title--services{left:21px;top:330px;font-size:16px}
  .tab-title--concierge{left:18px;top:12px;font-size:20px}
  .tab-rule{position:absolute;left:21px;top:42px;width:238px;height:3px;background:var(--white)}

  .checklist{position:absolute;list-style:none;font-family:"Montserrat",sans-serif;font-weight:700;color:var(--white)}
  .checklist li{position:relative;padding-left:20px}
  .checklist svg{position:absolute;left:0;top:0}
  .checklist--left,.checklist--right{font-size:12.5px;line-height:13px}
  .checklist--left{left:22px;top:374px;width:190px}
  .checklist--right{left:210px;top:374px;width:200px}
  .checklist--left li,.checklist--right li{margin-bottom:7px}
  .checklist--right li.more{font-family:"Roboto Condensed",sans-serif;font-size:12px;margin-bottom:0}
  .checklist--concierge{left:22px;top:84px;font-size:17px;line-height:24px}
  .checklist--concierge li{padding-left:26px}
  .checklist--concierge svg{top:2px}

  .monthly{position:absolute;left:21px;top:517px;font-family:"Fira Sans Condensed",sans-serif;font-weight:700;font-size:15px;color:var(--white);letter-spacing:.1px}
  .monthly span{font-weight:400;font-family:"Roboto Condensed",sans-serif}
  .contact{position:absolute;display:flex;align-items:center;gap:8px;color:var(--white);font-family:"Montserrat",sans-serif;font-weight:700}
  .contact--phone{left:19px;top:544px;font-size:17px}
  .contact--mail{left:241px;top:546px;font-size:14px}
  .call-note{position:absolute;left:22px;top:491px;font-size:14px;color:var(--white);font-weight:500}
  .call-note b{font-weight:700}
  .contact--phone-back{left:22px;top:535px;font-size:17px}
  .contact--mail-back{left:172px;top:536px;font-size:15.5px;font-family:"Roboto Condensed",sans-serif;font-weight:500}
</style>
</head>
<body>

<section class="card card--front">
  <div class="photo photo--park" role="img" aria-label="Photo of a tree-lined park path with two cyclists riding away"></div>
  <svg class="shapes" viewBox="0 0 853 568" aria-hidden="true">
    <polygon points="0,0 434,0 386,204 0,204" fill="var(--white)"/>
    <polygon points="434,0 482,0 442,204 386,204" fill="var(--red)"/>
    <polygon points="482,0 508,0 410,420 386,420" fill="var(--stripe)"/>
    <rect x="0" y="204" width="458" height="114" fill="var(--red)"/>
    <polygon points="0,318 400,318 470,540 0,540" fill="var(--wood)"/>
    <g stroke="var(--wood-dark)" stroke-width="1" opacity=".6">
      <line x1="0" y1="352" x2="415" y2="352"/><line x1="0" y1="384" x2="425" y2="384"/>
      <line x1="0" y1="416" x2="435" y2="416"/><line x1="0" y1="448" x2="445" y2="448"/>
      <line x1="0" y1="480" x2="455" y2="480"/>
    </g>
    <polygon points="400,318 430,318 500,540 470,540" fill="var(--red)"/>
    <polygon points="430,318 460,318 556,568 530,568" fill="var(--stripe)"/>
    <polygon points="0,320 250,320 238,364 0,364" fill="var(--ink)"/>
    <polygon points="0,508 390,508 406,540 0,540" fill="var(--red)"/>
    <polygon points="0,540 540,540 554,568 0,568" fill="var(--ink)"/>
  </svg>

  <div class="logo logo--front">
    <span class="logo__dot"></span>
    <div><div class="logo__name">Cedar Row</div><div class="logo__tag">MAINTENANCE &amp; CONCIERGE</div></div>
  </div>

  <p class="intro">We specialize in and provide residential maintenance and errand services to retired and semi retired persons living in the Lake Norman area</p>
  <h1 class="headline">CEDAR ROW MAINTENANCE<br>AND CONCIERGE SERVICE</h1>

  <h2 class="tab-title tab-title--services">The services we include</h2>
  <ul class="checklist checklist--left">
    <li><svg width="15" height="14" viewBox="0 0 15 14"><rect x="1" y="2" width="11" height="11" fill="none" stroke="#fff" stroke-width="2"/><path d="M3 7l3 3 8-9" fill="none" stroke="#fff" stroke-width="2.4"/></svg>Ceiling fan installation</li>
    <li><svg width="15" height="14" viewBox="0 0 15 14"><rect x="1" y="2" width="11" height="11" fill="none" stroke="#fff" stroke-width="2"/><path d="M3 7l3 3 8-9" fill="none" stroke="#fff" stroke-width="2.4"/></svg>Lighting and plumbing repairs</li>
    <li><svg width="15" height="14" viewBox="0 0 15 14"><rect x="1" y="2" width="11" height="11" fill="none" stroke="#fff" stroke-width="2"/><path d="M3 7l3 3 8-9" fill="none" stroke="#fff" stroke-width="2.4"/></svg>Ceiling fan installation</li>
    <li><svg width="15" height="14" viewBox="0 0 15 14"><rect x="1" y="2" width="11" height="11" fill="none" stroke="#fff" stroke-width="2"/><path d="M3 7l3 3 8-9" fill="none" stroke="#fff" stroke-width="2.4"/></svg>Handicap accessories</li>
    <li><svg width="15" height="14" viewBox="0 0 15 14"><rect x="1" y="2" width="11" height="11" fill="none" stroke="#fff" stroke-width="2"/><path d="M3 7l3 3 8-9" fill="none" stroke="#fff" stroke-width="2.4"/></svg>Locks and security</li>
  </ul>
  <ul class="checklist checklist--right">
    <li><svg width="15" height="14" viewBox="0 0 15 14"><rect x="1" y="2" width="11" height="11" fill="none" stroke="#fff" stroke-width="2"/><path d="M3 7l3 3 8-9" fill="none" stroke="#fff" stroke-width="2.4"/></svg>Picture hanging</li>
    <li><svg width="15" height="14" viewBox="0 0 15 14"><rect x="1" y="2" width="11" height="11" fill="none" stroke="#fff" stroke-width="2"/><path d="M3 7l3 3 8-9" fill="none" stroke="#fff" stroke-width="2.4"/></svg>Hang blinds</li>
    <li><svg width="15" height="14" viewBox="0 0 15 14"><rect x="1" y="2" width="11" height="11" fill="none" stroke="#fff" stroke-width="2"/><path d="M3 7l3 3 8-9" fill="none" stroke="#fff" stroke-width="2.4"/></svg>Furniture arrangement / assembly</li>
    <li><svg width="15" height="14" viewBox="0 0 15 14"><rect x="1" y="2" width="11" height="11" fill="none" stroke="#fff" stroke-width="2"/><path d="M3 7l3 3 8-9" fill="none" stroke="#fff" stroke-width="2.4"/></svg>Pressure washing</li>
    <li><svg width="15" height="14" viewBox="0 0 15 14"><rect x="1" y="2" width="11" height="11" fill="none" stroke="#fff" stroke-width="2"/><path d="M3 7l3 3 8-9" fill="none" stroke="#fff" stroke-width="2.4"/></svg>Battery Jump start</li>
    <li class="more">And More....</li>
  </ul>

  <p class="monthly">MONTHLY SERVICE <span>AGREEMENTS AND</span> 24/7 ACCESS</p>
  <p class="contact contact--phone"><svg width="19" height="19" viewBox="0 0 20 20"><circle cx="10" cy="10" r="10" fill="#fff"/><path d="M6.5 4.5l2.2 2.4-1.2 1.6c.8 1.7 1.9 2.9 3.6 3.8l1.5-1.2 2.4 2.2-1.4 2.2C9 15 5 11 4.6 6z" fill="var(--ink)"/></svg>704.555.0187</p>
  <p class="contact contact--mail"><svg width="19" height="19" viewBox="0 0 20 20"><circle cx="10" cy="10" r="10" fill="#fff"/><rect x="5" y="6.5" width="10" height="7" fill="var(--ink)"/><path d="M5 6.5l5 4 5-4" fill="none" stroke="#fff" stroke-width="1"/></svg>1cedarrowmaint@quillpostmail.com</p>
</section>

<section class="card card--back">
  <div class="photo photo--walk" role="img" aria-label="Photo of people walking along a paved path across a green lawn"></div>
  <svg class="shapes" viewBox="0 0 853 568" aria-hidden="true">
    <polygon points="0,0 390,0 442,238 0,238" fill="var(--red)"/>
    <polygon points="390,0 402,0 540,568 526,568" fill="var(--stripe)"/>
    <polygon points="0,0 382,0 370,54 0,54" fill="var(--ink)"/>
    <polygon points="0,480 515,480 528,568 0,568" fill="var(--wood)"/>
    <g stroke="var(--wood-dark)" stroke-width="1" opacity=".6">
      <line x1="0" y1="528" x2="520" y2="528"/><line x1="0" y1="552" x2="524" y2="552"/>
    </g>
    <polygon points="0,482 268,482 258,518 0,518" fill="var(--ink)"/>
  </svg>

  <h2 class="tab-title tab-title--concierge">Our Concierge Services include</h2>
  <span class="tab-rule"></span>
  <ul class="checklist checklist--concierge">
    <li><svg width="21" height="19" viewBox="0 0 15 14"><rect x="1" y="2" width="11" height="11" fill="none" stroke="#fff" stroke-width="2"/><path d="M3 7l3 3 8-9" fill="none" stroke="#fff" stroke-width="2.4"/></svg>Errand running</li>
    <li><svg width="21" height="19" viewBox="0 0 15 14"><rect x="1" y="2" width="11" height="11" fill="none" stroke="#fff" stroke-width="2"/><path d="M3 7l3 3 8-9" fill="none" stroke="#fff" stroke-width="2.4"/></svg>Grocery shopping</li>
    <li><svg width="21" height="19" viewBox="0 0 15 14"><rect x="1" y="2" width="11" height="11" fill="none" stroke="#fff" stroke-width="2"/><path d="M3 7l3 3 8-9" fill="none" stroke="#fff" stroke-width="2.4"/></svg>Wellness Checks</li>
    <li><svg width="21" height="19" viewBox="0 0 15 14"><rect x="1" y="2" width="11" height="11" fill="none" stroke="#fff" stroke-width="2"/><path d="M3 7l3 3 8-9" fill="none" stroke="#fff" stroke-width="2.4"/></svg>Dog Walk</li>
    <li><svg width="21" height="19" viewBox="0 0 15 14"><rect x="1" y="2" width="11" height="11" fill="none" stroke="#fff" stroke-width="2"/><path d="M3 7l3 3 8-9" fill="none" stroke="#fff" stroke-width="2.4"/></svg>Garbage Collection</li>
    <li>And More...</li>
  </ul>

  <p class="call-note">Call text or <b>E-mail</b> for more information</p>
  <p class="contact contact--phone-back"><svg width="19" height="19" viewBox="0 0 20 20"><circle cx="10" cy="10" r="10" fill="#fff"/><path d="M6.5 4.5l2.2 2.4-1.2 1.6c.8 1.7 1.9 2.9 3.6 3.8l1.5-1.2 2.4 2.2-1.4 2.2C9 15 5 11 4.6 6z" fill="var(--ink)"/></svg>704.555.0187</p>
  <p class="contact contact--mail-back"><svg width="19" height="19" viewBox="0 0 20 20"><circle cx="10" cy="10" r="10" fill="#fff"/><rect x="5" y="6.5" width="10" height="7" fill="var(--ink)"/><path d="M5 6.5l5 4 5-4" fill="none" stroke="#fff" stroke-width="1"/></svg>1cedarrowmaint@quillpostmail.com</p>

  <div class="logo logo--back">
    <span class="logo__dot"></span>
    <div><div class="logo__name">Cedar Row</div><div class="logo__tag">MAINTENANCE &amp; CONCIERGE</div></div>
  </div>
</section>

</body>
</html>
```